Website design for lighting products company

We want a design for our website. The website is for a company that sells lighting products. The structure is similar to the below website. We really like their design as well: www.ambervalelamps.com

Industry/Entity Type

Lighting

Number of Pages Required

5+ page

Colors

Designer to choose colors to be used in the design.

Requirements
Must have
• Simple design

```html
<!DOCTYPE html>
<html lang="en">
<head>
<meta charset="utf-8">
<title>Keel Lighting</title>
<link rel="stylesheet" href="https://fonts.googleapis.com/css2?family=Quicksand:wght@400;500;600&family=Arimo:wght@400&display=swap">
<style>
:root{
  --orange:#f47c14;
  --orange-deep:#ef6f0a;
  --ink:#222222;
  --text:#555555;
  --muted:#8a8a8a;
  --line:#e3e3e3;
  --dark:#161616;
  --dark-band:#262626;
  --light:#f1f1f1;
  --white:#ffffff;
}
*{box-sizing:border-box;margin:0;padding:0}
html,body{width:1200px;height:3288px;overflow:hidden}
body{position:relative;background:var(--white);font-family:'Arimo',Arial,sans-serif;color:var(--text)}
.abs{position:absolute}
.q{font-family:'Quicksand',Arial,sans-serif}

/* header */
.brand{left:111px;top:36px;font-size:32px;font-weight:500;color:var(--ink)}
.nav{top:54px;left:0;width:1200px;font-family:'Quicksand',sans-serif;font-size:12px;font-weight:600;color:var(--ink)}
.nav span{position:absolute;top:0;white-space:nowrap}
.nav .active{color:var(--orange)}

/* hero */
.hero{left:0;top:113px;width:1200px;height:682px;background:linear-gradient(180deg,#b8a58a 0%,#6d5a45 45%,#3b3028 75%,#5e5147 100%)}
.hero-box{left:341px;top:239px;width:518px;height:296px;background:rgba(40,40,40,.72);text-align:center;color:var(--white)}
.hero-title{position:absolute;left:0;width:100%;top:44px;font-size:44px;font-weight:500}
.hero-sub{position:absolute;left:0;width:100%;top:116px;font-size:19px;line-height:33px;font-weight:500}
.btn-slant{position:absolute;width:154px;height:54px;font-family:'Quicksand',sans-serif;font-size:17px;font-weight:600;text-align:center;line-height:54px}
.btn-slant svg{position:absolute;left:0;top:0}
.btn-slant span{position:relative}

/* headings */
.h2{left:0;width:1200px;text-align:center;font-family:'Quicksand',sans-serif;font-size:34px;font-weight:400;color:var(--ink)}
.rule{height:2px;width:64px;left:568px;background:var(--orange)}
.para{left:250px;width:700px;text-align:center;font-size:14px;line-height:31px;color:var(--text)}

/* works */
.work{width:230px;height:220px;top:1423px;border:3px solid #f6b27a}
.work-title{width:250px;top:1660px;text-align:center;font-family:'Quicksand',sans-serif;font-size:22px;font-weight:500;color:var(--white)}
.work-sub{width:250px;top:1696px;text-align:center;font-size:14px;color:#fff3e6}

/* products */
.product{width:231px;height:241px;border:2px solid var(--line);background:var(--white);box-shadow:0 1px 3px rgba(0,0,0,.06)}
.product .pic{position:absolute;left:30px;top:18px;width:167px;height:150px;border-radius:6px;background:radial-gradient(circle,#e9e9e9 0%,#f7f7f7 70%)}
.product .label{position:absolute;left:0;width:100%;top:178px;text-align:center;font-family:'Quicksand',sans-serif;font-size:16px;font-weight:500;color:#444}

/* newsletter */
.news{left:0;top:2557px;width:1200px;height:323px;background:linear-gradient(180deg,#eeeeee,#f6f6f6 50%,#ececec)}
.field{background:var(--white);border:1px solid #d8d8d8;font-size:13px;color:#333;padding-left:14px}

/* footer */
.footer{left:0;top:2880px;width:1200px;height:408px;background:var(--dark)}
.f-head{top:2928px;font-family:'Quicksand',sans-serif;font-size:21px;font-weight:600;color:var(--white);letter-spacing:.5px}
.f-in{background:var(--white);font-size:11px;color:#333;padding:10px 0 0 12px}
.f-icon{width:42px;height:42px;border:2px solid #ddd;border-radius:50%}
.f-lbl{font-family:'Quicksand',sans-serif;font-size:13px;font-weight:600;color:var(--white)}
.f-txt{font-family:'Quicksand',sans-serif;font-size:12px;color:#bdbdbd;line-height:19px}
.f-link{left:932px;font-family:'Quicksand',sans-serif;font-size:12px;font-weight:600;color:var(--white)}
.f-arrow{left:900px;font-size:12px;color:var(--white)}
.social{width:36px;height:36px;border:2px solid #ddd;border-radius:50%;top:3234px}
.copyright{left:111px;top:3245px;font-size:12px;color:#d0d0d0}
</style>
</head>
<body>

<!-- header -->
<div class="abs brand q">Keel Lighting</div>
<nav class="abs nav">
  <span class="active" style="left:514px">HOME</span>
  <span style="left:590px">ABOUT US</span>
  <span style="left:693px">SERVICES</span>
  <span style="left:791px">PRODUCTS</span>
  <span style="left:898px">SOLUTIONS</span>
  <span style="left:1009px">CONTACT US</span>
</nav>

<!-- hero -->
<div class="abs hero" role="img" aria-label="Photo of a warmly lit hotel lounge with sofas, lamps and a slatted ceiling"></div>
<div class="abs hero-box">
  <div class="hero-title q">Keel Lighting</div>
  <div class="hero-sub q">Sed ut perspiciatis unde omnis iste natus error<br>voluptatem accusantium dolorem</div>
  <div class="btn-slant" style="left:182px;top:207px;color:var(--white)">
    <svg width="154" height="54"><polygon points="14,0 154,0 140,54 0,54" fill="var(--orange)"/></svg>
    <span>Read More</span>
  </div>
</div>

<!-- welcome -->
<div class="abs h2" style="top:848px">Welcome to Keel Lighting</div>
<div class="abs rule" style="top:913px"></div>
<p class="abs para" style="top:935px">Sed ut perspiciatis unde omnis iste natus error sit voluptatem accusantium doloremque laudantium, totam rem aperiam, eaque ipsa quae ab illo inventore veritatis et quasi architecto beatae vitae dicta sunt explicabo. Nemo enim ipsam voluptatem quia voluptas sit aspernatur aut odit aut fugit, sed quia consequuntur magni dolores eos accusantium doloremque qui ratione voluptatem sequi nesciunt.</p>
<div class="abs btn-slant" style="left:523px;top:1084px;color:var(--orange)">
  <svg width="154" height="56"><polygon points="14,1 153,1 139,55 1,55" fill="none" stroke="var(--orange)" stroke-width="1.2"/></svg>
  <span>Read More</span>
</div>

<!-- works band -->
<svg class="abs" style="left:0;top:1160px" width="1200" height="700" aria-hidden="true">
  <polygon points="0,63 420,100 0,130" fill="var(--dark-band)"/>
  <polygon points="760,628 1200,602 1200,651" fill="var(--dark-band)"/>
  <polygon points="0,129 1200,8 1200,616 0,691" fill="var(--orange-deep)"/>
</svg>
<div class="abs h2" style="top:1294px;color:var(--white);font-size:36px">Our Works</div>
<div class="abs" style="left:0;width:1200px;top:1358px;text-align:center;font-size:14px;color:#fff3e6">Sed ut perspiciatis unde omnis iste natus error sit voluptatem accusantium doloremque laudantium, totam rem</div>

<div class="abs work" style="left:112px;background:linear-gradient(160deg,#d8d6cf,#b9683a 70%,#6e5a4a)" role="img" aria-label="Office lounge with orange armchairs"></div>
<div class="abs work" style="left:361px;background:linear-gradient(180deg,#8b949a,#d9dde0 55%,#c3c9cd)" role="img" aria-label="Long school corridor with linear ceiling lights"></div>
<div class="abs work" style="left:610px;background:linear-gradient(180deg,#d7d9dc,#9aa0a6 55%,#3c3436)" role="img" aria-label="Hospital meeting room with a dark conference table"></div>
<div class="abs work" style="left:858px;background:linear-gradient(180deg,#c9b79a,#e4d6bf 55%,#8c7b68)" role="img" aria-label="Residential hall with warm ceiling light"></div>

<div class="abs work-title" style="left:106px">Workspace</div>
<div class="abs work-title" style="left:351px">Education</div>
<div class="abs work-title" style="left:602px">Healthcare</div>
<div class="abs work-title" style="left:851px">Residential</div>
<div class="abs work-sub" style="left:102px">Sed ut perspiciatis unde omnis</div>
<div class="abs work-sub" style="left:351px">Sed ut perspiciatis unde omnis</div>
<div class="abs work-sub" style="left:599px">Sed ut perspiciatis unde omnis</div>
<div class="abs work-sub" style="left:848px">Sed ut perspiciatis unde omnis</div>

<!-- products -->
<div class="abs h2" style="top:1855px">Our Products</div>
<div class="abs rule" style="top:1922px"></div>

<div class="abs product" style="left:111px;top:1974px"><div class="pic" role="img" aria-label="Twin glass wall lamp"></div><div class="label">Sed ut perspiciatis</div></div>
<div class="abs product" style="left:360px;top:1974px"><div class="pic" role="img" aria-label="Brass wall sconce"></div><div class="label">Sed ut perspiciatis</div></div>
<div class="abs product" style="left:609px;top:1974px"><div class="pic" role="img" aria-label="Spiral energy saving bulb"></div><div class="label">Sed ut perspiciatis</div></div>
<div class="abs product" style="left:858px;top:1974px"><div class="pic" role="img" aria-label="Square LED panel light"></div><div class="label">Sed ut perspiciatis</div></div>
<div class="abs product" style="left:111px;top:2239px"><div class="pic" role="img" aria-label="Compact fluorescent tube"></div><div class="label">Sed ut perspiciatis</div></div>
<div class="abs product" style="left:360px;top:2239px"><div class="pic" role="img" aria-label="Clear incandescent bulb"></div><div class="label">Sed ut perspiciatis</div></div>
<div class="abs product" style="left:609px;top:2239px"><div class="pic" role="img" aria-label="Double bowl wall light"></div><div class="label">Sed ut perspiciatis</div></div>
<div class="abs product" style="left:858px;top:2239px"><div class="pic" role="img" aria-label="Tall black frame lamp"></div><div class="label">Sed ut perspiciatis</div></div>

<!-- newsletter -->
<div class="abs news"></div>
<div class="abs h2" style="top:2610px">Subscribe to Our Newsletter</div>
<div class="abs" style="left:568px;top:2650px;width:65px;height:2px;background:var(--orange)"></div>
<div class="abs" style="left:0;width:1200px;top:2696px;text-align:center;font-size:14px;color:var(--text)">Sed ut perspiciatis unde omnis iste natus error sit voluptatem accusantium doloremque laudantium, totam rem aperiam</div>
<div class="abs field" style="left:221px;top:2756px;width:631px;height:56px;line-height:54px">Enter Your Email :</div>
<div class="abs" style="left:851px;top:2756px;width:128px;height:56px;line-height:56px;background:var(--orange);color:var(--white);text-align:center;font-size:14px">SUBSCRIBE</div>

<!-- footer -->
<div class="abs footer"></div>
<div class="abs f-head" style="left:117px">CONTACT US</div>
<div class="abs f-head" style="left:582px">ADDRESS</div>
<div class="abs f-head" style="left:897px">LINKS</div>

<div class="abs f-in" style="left:117px;top:2982px;width:180px;height:36px">First Name :</div>
<div class="abs f-in" style="left:308px;top:2982px;width:180px;height:36px">Last Name :</div>
<div class="abs f-in" style="left:117px;top:3026px;width:180px;height:36px">Email :</div>
<div class="abs f-in" style="left:308px;top:3026px;width:180px;height:36px">Phone :</div>
<div class="abs f-in" style="left:117px;top:3070px;width:371px;height:53px">Message :</div>
<div class="abs" style="left:117px;top:3131px;width:97px;height:36px;line-height:36px;background:var(--orange);color:var(--white);text-align:center;font-size:13px">SUBMIT</div>

<div class="abs f-icon" style="left:575px;top:2978px"><svg width="38" height="38" viewBox="0 0 38 38"><path d="M19 11a5 5 0 0 0-5 5c0 4 5 10 5 10s5-6 5-10a5 5 0 0 0-5-5zm0 7a2 2 0 1 1 0-4 2 2 0 0 1 0 4z" fill="#fff"/></svg></div>
<div class="abs f-lbl" style="left:632px;top:2982px">ADDRESS</div>
<div class="abs f-txt" style="left:632px;top:3000px">#154 Lorem Ipsum dummy<br>Text Lorem Dummy</div>

<div class="abs f-icon" style="left:575px;top:3061px"><svg width="38" height="38" viewBox="0 0 38 38"><path d="M14 12l3 0 1.5 4-2 1.3a9 9 0 0 0 4.2 4.2l1.3-2 4 1.5 0 3c0 1-1 2-2 2A13 13 0 0 1 12 14c0-1 1-2 2-2z" fill="#fff"/></svg></div>
<div class="abs f-lbl" style="left:634px;top:3066px">PHONE NUMBER</div>
<div class="abs f-txt" style="left:634px;top:3086px">000-482-7306</div>

<div class="abs f-icon" style="left:575px;top:3128px"><svg width="38" height="38" viewBox="0 0 38 38"><rect x="11" y="13" width="16" height="12" rx="1.5" fill="#fff"/><path d="M11 14l8 6 8-6" fill="none" stroke="var(--dark)" stroke-width="1.4"/></svg></div>
<div class="abs f-lbl" style="left:634px;top:3131px">EMAIL US</div>
<div class="abs f-txt" style="left:634px;top:3150px">info@keellighting.com</div>

<div class="abs f-arrow" style="top:2974px">»</div><div class="abs f-link" style="top:2975px">HOME</div>
<div class="abs f-arrow" style="top:3009px">»</div><div class="abs f-link" style="top:3010px">ABOUT US</div>
<div class="abs f-arrow" style="top:3044px">»</div><div class="abs f-link" style="top:3045px">SERVICES</div>
<div class="abs f-arrow" style="top:3079px">»</div><div class="abs f-link" style="top:3080px">PRODUCTS</div>
<div class="abs f-arrow" style="top:3114px">»</div><div class="abs f-link" style="top:3115px">SOLUTIONS</div>
<div class="abs f-arrow" style="top:3149px">»</div><div class="abs f-link" style="top:3150px">CONTACT US</div>

<div class="abs" style="left:111px;top:3214px;width:978px;height:1px;background:#333"></div>
<div class="abs copyright">© Copyright 2019 Keel Lighting..All Rights Reserved</div>
<div class="abs social" style="left:881px"></div>
<div class="abs social" style="left:923px"></div>
<div class="abs social" style="left:966px"></div>
<div class="abs social" style="left:1008px"></div>
<div class="abs social" style="left:1051px"></div>

</body>
</html>
```